Holbys Pet Care

Hi. I need a business card /logo for my pet care business. Im thinking about a dogs paw print. Although i do look after other pets so don't want to restrict my self. Open to suggestions on colour etc but like greens and purples.The name of my business is holby's pet care. The logo could be just an image or have holbys power care on it. An option to do either would be great. For the winner i also would like a Web page (word press template if possible) designed if you can, of course I'll pay additional for this. Look forward to your ideas!

```html
<!DOCTYPE html>
<html lang="en">
<head>
<meta charset="utf-8">
<title>Holby's Pet Care – Business Card</title>
<link href="https://fonts.googleapis.com/css2?family=Ubuntu:wght@400;500;700&display=swap" rel="stylesheet">
<style>
  :root {
    --page-bg: #e6e4e1;
    --card-white: #f7f7f7;
    --brand-purple: #6f3d97;
    --brand-green: #b5e61d;
    --ink: #2b2b2b;
    --ink-soft: #555555;
    --on-purple: #ffffff;
  }
  * { box-sizing: border-box; margin: 0; padding: 0; }
  html, body {
    width: 1200px;
    height: 899px;
    overflow: hidden;
    background: var(--page-bg);
    font-family: "Ubuntu", sans-serif;
  }
  .card {
    position: absolute;
    left: 180px;
    top: 210px;
    width: 840px;
    height: 480px;
    border-radius: 40px;
    overflow: hidden;
    background: linear-gradient(160deg, #ffffff 0%, var(--card-white) 55%, #ececec 100%);
    box-shadow: 0 14px 36px rgba(0,0,0,0.18);
  }
  .card-waves {
    position: absolute;
    inset: 0;
    width: 100%;
    height: 100%;
  }
  .brand {
    position: absolute;
    left: 0;
    right: 0;
    top: 92px;
    display: flex;
    justify-content: center;
    align-items: center;
    gap: 16px;
  }
  .brand-dot {
    width: 40px;
    height: 40px;
    border-radius: 50%;
    background: var(--brand-purple);
    flex: none;
  }
  .brand-name {
    font-family: "Ubuntu", sans-serif;
    font-weight: 500;
    font-size: 40px;
    line-height: 1;
    color: var(--brand-purple);
    white-space: nowrap;
  }
  .holder {
    position: absolute;
    left: 305px;
    top: 200px;
    width: 230px;
    text-align: center;
  }
  .holder-name {
    font-weight: 500;
    font-size: 22px;
    color: var(--ink);
    letter-spacing: 1.5px;
  }
  .holder-role {
    font-size: 14px;
    color: var(--ink-soft);
    margin-top: 3px;
  }
  .contacts {
    position: absolute;
    left: 30px;
    top: 262px;
    list-style: none;
  }
  .contact {
    display: flex;
    align-items: center;
    gap: 10px;
    height: 26px;
    font-size: 13px;
    color: var(--on-purple);
  }
  .contact-icon {
    width: 17px;
    height: 17px;
    flex: none;
  }
</style>
</head>
<body>
  <div class="card">
    <svg class="card-waves" viewBox="0 0 840 480" preserveAspectRatio="none" aria-hidden="true">
      <path fill="var(--brand-green)" d="M0 175 C160 215 300 325 520 305 C650 293 760 250 840 215 L840 250 C760 282 650 322 520 330 C300 345 150 232 0 198 Z"/>
      <path fill="var(--brand-purple)" d="M0 212 C150 248 300 362 520 345 C650 335 760 295 840 270 L840 480 L0 480 Z"/>
    </svg>

    <div class="brand">
      <span class="brand-dot"></span>
      <p class="brand-name">Holby's Pet Care</p>
    </div>

    <div class="holder">
      <p class="holder-name">PETER LANGFORD</p>
      <p class="holder-role">Managing Director</p>
    </div>

    <ul class="contacts">
      <li class="contact">
        <svg class="contact-icon" viewBox="0 0 20 20"><circle cx="10" cy="10" r="10" fill="#fff"/><path fill="var(--brand-purple)" d="M7 5 L9 7.5 L8 9 C9 11 10 12 11 12 L12.5 11 L15 13 L13.5 15 C9.5 15 5 10.5 5 6.5 Z"/></svg>
        <span>014 782 3051</span>
      </li>
      <li class="contact">
        <svg class="contact-icon" viewBox="0 0 20 20"><circle cx="10" cy="10" r="10" fill="#fff"/><path fill="var(--brand-purple)" d="M7 5 L9 7.5 L8 9 C9 11 10 12 11 12 L12.5 11 L15 13 L13.5 15 C9.5 15 5 10.5 5 6.5 Z"/></svg>
        <span>014 782 3052</span>
      </li>
      <li class="contact">
        <svg class="contact-icon" viewBox="0 0 20 20"><circle cx="10" cy="10" r="10" fill="#fff"/><rect x="5" y="6.5" width="10" height="7" fill="none" stroke="var(--brand-purple)" stroke-width="1.4"/><path d="M5 6.5 L10 10.5 L15 6.5" fill="none" stroke="var(--brand-purple)" stroke-width="1.4"/></svg>
        <span>hello@holbyspets.com</span>
      </li>
      <li class="contact">
        <svg class="contact-icon" viewBox="0 0 20 20"><circle cx="10" cy="10" r="10" fill="#fff"/><circle cx="10" cy="10" r="5" fill="none" stroke="var(--brand-purple)" stroke-width="1.3"/><path d="M5 10 H15 M10 5 C7.5 8 7.5 12 10 15 C12.5 12 12.5 8 10 5" fill="none" stroke="var(--brand-purple)" stroke-width="1.1"/></svg>
        <span>www.holbyspets.com</span>
      </li>
      <li class="contact">
        <svg class="contact-icon" viewBox="0 0 20 20"><circle cx="10" cy="10" r="10" fill="#fff"/><path fill="var(--brand-purple)" d="M10 4 C7.5 4 6 5.8 6 8 C6 11 10 16 10 16 C10 16 14 11 14 8 C14 5.8 12.5 4 10 4 Z"/><circle cx="10" cy="8" r="1.6" fill="#fff"/></svg>
        <span>27 Meadow Lane Harbury HB4</span>
      </li>
    </ul>
  </div>
</body>
</html>
```